Taskvora Software Business Card Design

We are a new organization called Taskvora. We are a software as a service provider. We deliver a project and program management solution via the internet, so everyone has the ability to work together and collaborate. Its an enterprise platform and we will focus on 50 plus employee company.

We have a website in place
www.taskvora-example.com

Use this as a start of producing the business card. The logo is there as well, but if you have a great and better solution...

Color scheme's could be inline with the website, but don't pin point on it. We can always change the website, logo, color scheme etc.

Target Market(s)

B2B, Projectmembers, projectmanagers, ICT, CTO, Marketing Managers

Industry/Entity Type

Software

Requirements
Must have
• Maarten Velsepol

Tel: +31 555 17 40 92
Mob: +31 6 902 36 517
maarten@taskvora-example.com
Keltenlaan 384b
9071 XK Zandlinden

Www.taskvora-example.com
social media links

```html
<!DOCTYPE html>
<html lang="en">
<head>
<meta charset="utf-8">
<title>Taskvora Business Card</title>
<link href="https://fonts.googleapis.com/css2?family=Exo+2:wght@300&family=Open+Sans:wght@300;400;700&display=swap" rel="stylesheet">
<style>
  :root {
    --page: #0a0b0d;
    --card: #2a2e37;
    --panel: #222429;
    --texture: #30343d;
    --texture-dark: #272a31;
    --green: #97a048;
    --white: #ffffff;
    --muted: #b9bcc4;
    --arrow-dark: #1c1e22;
  }
  * { margin: 0; padding: 0; box-sizing: border-box; }
  html, body { width: 861px; height: 1200px; overflow: hidden; background: var(--page); }
  body { position: relative; font-family: "Open Sans", sans-serif; }
  .card { position: absolute; left: 145px; width: 572px; height: 343px; background: var(--card); overflow: hidden; }
  .card--front { top: 129px; }
  .card--back { top: 725px; }
  .block { position: absolute; }

  /* front */
  .logo-band { left: 0; top: 70px; width: 318px; height: 71px; background: var(--panel); }
  .logo-texture { left: 318px; top: 70px; width: 161px; height: 71px; background: var(--texture); }
  .logo-name { position: absolute; left: 50px; top: 82px; font-family: "Exo 2", sans-serif; font-weight: 300; font-size: 44px; line-height: 1; color: var(--white); letter-spacing: 0.5px; }
  .role-band { left: 0; top: 141px; width: 572px; height: 121px; background: var(--green); }
  .roles { position: absolute; left: 48px; top: 170px; list-style: none; }
  .roles li { position: relative; padding-left: 27px; font-weight: 700; font-size: 14px; line-height: 20.5px; color: var(--white); }
  .roles svg { position: absolute; left: 0; top: 6px; }
  .address-texture { left: 183px; top: 262px; width: 296px; height: 81px; background: var(--texture-dark); }
  .address { position: absolute; left: 47px; top: 278px; font-weight: 300; font-size: 13px; line-height: 17px; color: var(--muted); }

  /* back */
  .top-texture { left: 0; top: 0; width: 170px; height: 75px; background: var(--texture-dark); }
  .name-panel { left: 0; top: 73px; width: 479px; height: 210px; background: var(--panel); }
  .bottom-texture { left: 125px; top: 266px; width: 290px; height: 17px; background: var(--texture); }
  .person { position: absolute; left: 72px; top: 97px; font-size: 25px; font-weight: 400; color: var(--white); white-space: nowrap; display: flex; align-items: center; gap: 14px; }
  .person .first { color: var(--green); }
  .contact-box { left: 0; top: 146px; width: 310px; height: 85px; background: var(--green); }
  .contact-box-foot { left: 0; top: 231px; width: 241px; height: 35px; background: var(--green); }
  .contact { position: absolute; left: 72px; top: 170px; font-weight: 300; font-size: 15px; line-height: 21px; color: var(--white); white-space: nowrap; }
  .contact-arrow { position: absolute; left: 45px; top: 198px; }
</style>
</head>
<body>

<section class="card card--front">
  <div class="block logo-band"></div>
  <div class="block logo-texture" role="img" aria-label="Diagonal stripe texture"></div>
  <div class="logo-name">Taskvora</div>
  <div class="block role-band"></div>
  <ul class="roles">
    <li><svg width="10" height="9" viewBox="0 0 10 9"><path d="M1 1l6 3.5L1 8" fill="none" stroke="#fff" stroke-width="1.8"/></svg>Team Member</li>
    <li><svg width="10" height="9" viewBox="0 0 10 9"><path d="M1 1l6 3.5L1 8" fill="none" stroke="#fff" stroke-width="1.8"/></svg>Project Manager</li>
    <li><svg width="10" height="9" viewBox="0 0 10 9"><path d="M1 1l6 3.5L1 8" fill="none" stroke="#fff" stroke-width="1.8"/></svg>Management</li>
  </ul>
  <div class="block address-texture" role="img" aria-label="Diagonal stripe texture"></div>
  <p class="address">Keltenlaan 384b<br>9071 XK Zandlinden</p>
</section>

<section class="card card--back">
  <div class="block top-texture" role="img" aria-label="Diagonal stripe texture"></div>
  <div class="block name-panel"></div>
  <div class="block bottom-texture" role="img" aria-label="Diagonal stripe texture"></div>
  <div class="person">
    <span><span class="first">Maarten</span> Velsepol</span>
    <svg width="18" height="12" viewBox="0 0 18 12"><path d="M2 1l6 5-6 5" fill="none" stroke="#97a048" stroke-width="2"/><path d="M9 1l6 5-6 5" fill="none" stroke="#fff" stroke-width="2"/></svg>
  </div>
  <div class="block contact-box"></div>
  <div class="block contact-box-foot"></div>
  <svg class="contact-arrow" width="18" height="12" viewBox="0 0 18 12"><path d="M2 1l6 5-6 5" fill="none" stroke="#1c1e22" stroke-width="2"/><path d="M9 1l6 5-6 5" fill="none" stroke="#fff" stroke-width="2"/></svg>
  <p class="contact">(31) 555 174 092<br>maarten@taskvora-example.com<br>www.taskvora-example.com</p>
</section>

</body>
</html>
```